Business card for law firm

Need business card for new law firm. Think confident, authoritative, conservative, but not stuffy or old-fashioned.

Contact Information for Business Card

Content for card - logo (uploaded), plus the following:

Paul Wexbury (larger font)
Managing Partner (larger font, but not as large as name)
Level 9, 41 Tansy Lane
Sydney NSW 2000
Main Tel 02 7346 2190
Direct Tel 02 6273 4415
Email paul@qvlegal.com.au
www.qvlegal.com.au

Letterhead design should include logo plus:
Level 9, 41 Tansy Lane
Sydney NSW 2000
Tel 02 6273 4415
www.qvlegal.com.au

```html
<!DOCTYPE html>
<html lang="en">
<head>
<meta charset="utf-8">
<title>Quayvale Legal – Business Card</title>
<link rel="stylesheet" href="https://fonts.googleapis.com/css2?family=Cinzel:wght@400&family=Open+Sans:wght@400;700&family=Poppins:wght@500&family=Michroma&display=swap">
<style>
  :root {
    --page: #ffffff;
    --backdrop: #0b0c0e;
    --brand: #363069;
    --paper: #ffffff;
    --ink: #1c1a1a;
  }
  * { margin: 0; padding: 0; box-sizing: border-box; }
  html, body {
    width: 1200px; height: 1200px; overflow: hidden;
    background: var(--page);
  }
  .canvas { position: relative; width: 1200px; height: 1200px; }
  .backdrop {
    position: absolute; left: 255px; top: 157px; width: 719px; height: 856px;
    background: var(--backdrop);
  }
  .card {
    position: absolute; left: 364px; width: 525px; height: 300px;
    border-radius: 36px; overflow: hidden;
  }
  .card--front { top: 262px; background: var(--brand); color: var(--paper); }
  .card--back { top: 608px; background: var(--paper); color: var(--brand); }

  .person { position: absolute; text-align: center; width: 240px; }
  .person__name {
    font-family: "Open Sans", sans-serif; font-weight: 700;
    font-size: 24px; line-height: 1; letter-spacing: -0.2px;
  }
  .person__role {
    font-family: "Open Sans", sans-serif; font-weight: 400;
    font-size: 10.5px; line-height: 1; margin-top: 5px; letter-spacing: -0.2px;
  }
  .card--front .person { left: 288px; top: 18px; }
  .card--back .person { left: 292px; top: 28px; color: var(--ink); }

  .brand { position: absolute; text-align: center; font-family: "Cinzel", serif; font-weight: 400; }
  .brand__mark { display: block; margin: 0 auto; }
  .brand__name { display: block; line-height: 1; }
  .brand__sub { display: block; line-height: 1; }

  .card--front .brand { left: 113px; top: 62px; width: 280px; }
  .card--front .brand__mark { width: 70px; height: 70px; background: var(--paper); margin-bottom: 26px; }
  .card--front .brand__name { font-size: 42px; }
  .card--front .brand__sub { font-size: 26px; letter-spacing: 9px; margin-top: 2px; padding-left: 9px; }

  .card--back .brand { left: 20px; top: 91px; width: 220px; }
  .card--back .brand__mark { width: 56px; height: 56px; background: var(--brand); margin-bottom: 20px; }
  .card--back .brand__name { font-size: 31px; }
  .card--back .brand__sub { font-size: 19px; letter-spacing: 6px; margin-top: 1px; padding-left: 6px; }

  .web {
    position: absolute; left: 0; width: 525px; top: 264px; text-align: center;
    font-family: "Michroma", sans-serif; font-size: 15px; letter-spacing: 10px;
    padding-left: 10px; line-height: 1;
  }

  .contact {
    position: absolute; left: 268px; top: 104px; list-style: none;
    font-family: "Poppins", sans-serif; font-weight: 500;
    font-size: 16.5px; line-height: 21.3px; letter-spacing: -0.2px;
  }
</style>
</head>
<body>
<div class="canvas">
  <div class="backdrop"></div>

  <section class="card card--front">
    <div class="person">
      <p class="person__name">Paul Wexbury</p>
      <p class="person__role">MANAGING PARTNER</p>
    </div>
    <div class="brand">
      <span class="brand__mark"></span>
      <span class="brand__name">QUAYVALE</span>
      <span class="brand__sub">LEGAL</span>
    </div>
    <p class="web">WWW.QVLEGAL.COM.AU</p>
  </section>

  <section class="card card--back">
    <div class="person">
      <p class="person__name">Paul Wexbury</p>
      <p class="person__role">MANAGING PARTNER</p>
    </div>
    <div class="brand">
      <span class="brand__mark"></span>
      <span class="brand__name">QUAYVALE</span>
      <span class="brand__sub">LEGAL</span>
    </div>
    <ul class="contact">
      <li>Level 9, 41 Tansy Lane</li>
      <li>Sydney NSW 2000</li>
      <li>Main Tel 02 7346 2190</li>
      <li>Direct Tel 02 6273 4415</li>
      <li>Email paul@qvlegal.com.au</li>
      <li>www.qvlegal.com.au</li>
    </ul>
  </section>
</div>
</body>
</html>
```